Flu Brochure- brief and easy-to-read

A team of health educators is looking to design a brochure on what Americans need to "know and do" when it comes to flu season. All copy and images will be provided.

The brochure needs to be an 8.5 x 11 inch bi-fold design.

I am only able to upload up to 5 files. So, additional images will have to sent via dropbox or some other mechanism.

Target Market(s)

The audience is vast, but the content and design need to be simple and engaging.

Industry/Entity Type

Health

Requirements
Must have
• Must Have:
- Clear and Simple, Easy-to-read and Understand and Act on- should be very focused on what the consumer should do about taking care of themselves when it comes to the flu.

We will provide all of the copy for the brochure design. We will also provide photographs for the project.

Captions for photographs that support the key message.

Should Not Have:
- x reverse print- e.g., no white font on a black background
x fancy fonts or heavy use of italics
x use of all capitals
x no full justification
x no use of drop caps

Must be multicultural as well.

```html
<!DOCTYPE html>
<html lang="en">
<head>
<meta charset="utf-8">
<title>Flu – Know and Do brochure</title>
<link rel="stylesheet" href="https://fonts.googleapis.com/css2?family=Arimo:wght@400&family=Questrial&display=swap">
<style>
  :root {
    --sky: #29a8e0;
    --navy: #0f62a8;
    --paper: #ffffff;
    --ink: #1f1f1f;
    --brand-red: #d4203f;
    --stage: #e6e6e6;
  }
  * { margin: 0; padding: 0; box-sizing: border-box; }
  html, body { width: 1200px; height: 960px; overflow: hidden; background: var(--stage); }
  .canvas { position: relative; width: 1200px; height: 960px; }
  .spread {
    position: absolute; left: 6px; top: 96px; width: 1188px; height: 768px;
    font-family: "Arimo", Arial, sans-serif; color: var(--ink);
    box-shadow: 0 4px 18px rgba(0,0,0,.25);
  }
  .panel { position: absolute; top: 0; width: 594px; height: 768px; overflow: hidden; }
  .panel--back { left: 0; background: var(--sky); }
  .panel--front { left: 594px; background: var(--paper); }
  .shapes { position: absolute; inset: 0; }

  .photo { position: absolute; }
  .photo--children {
    left: 62px; top: 126px; width: 467px; height: 433px;
    background: radial-gradient(ellipse at 50% 55%, #e8d6c4 0%, #f3ece4 40%, #ffffff 70%);
  }
  .photo--patient {
    left: 0; top: 0; width: 594px; height: 340px;
    background: linear-gradient(100deg, #d9d6d2 0%, #b99b83 35%, #8a7b70 55%, #d8cfc6 80%, #eef0ea 100%);
  }

  .resources {
    position: absolute; left: 0; width: 594px; top: 602px; text-align: center;
    color: var(--paper); font-size: 15px; line-height: 19px;
  }

  .sponsor { position: absolute; display: flex; align-items: center; gap: 14px; }
  .sponsor__label { font-size: 10.5px; color: #333; }
  .sponsor__name { font-size: 19px; color: var(--brand-red); }
  .panel--back .sponsor { left: 40px; top: 724px; }
  .panel--front .sponsor { left: 38px; top: 706px; }

  .section-title {
    position: absolute; left: 297px; top: 350px;
    font-family: "Questrial", Arial, sans-serif; font-size: 32px; letter-spacing: 2px;
    color: var(--paper); font-weight: 400;
  }
  .question {
    position: absolute; left: 39px; top: 505px; font-size: 18px; line-height: 23px; color: var(--ink);
  }
  .steps { position: absolute; left: 370px; top: 430px; list-style: none; }
  .steps__item {
    display: flex; align-items: center; gap: 7px;
    font-family: "Questrial", Arial, sans-serif; font-size: 38px; line-height: 44px; color: var(--sky);
  }
  .steps__item::before {
    content: ""; width: 12px; height: 12px; border: 3px solid #bdbdbd; background: #e6e6e6;
  }
  .credits {
    position: absolute; left: 38px; top: 649px; width: 510px; font-size: 11px; line-height: 14px; color: #222;
  }
  .web {
    position: absolute; left: 369px; top: 730px; font-size: 15px; color: var(--paper);
  }
</style>
</head>
<body>
<div class="canvas">
  <div class="spread">

    <section class="panel panel--back">
      <svg class="shapes" width="594" height="768" viewBox="0 0 594 768">
        <rect x="0" y="340" width="62" height="58" fill="#ffffff"/>
        <rect x="0" y="397" width="62" height="6" fill="#0f62a8"/>
        <rect x="529" y="340" width="65" height="22" fill="#ffffff"/>
        <rect x="529" y="362" width="65" height="5" fill="#0f62a8"/>
        <polygon points="0,712 311,712 346,748 346,768 0,768" fill="#ffffff"/>
      </svg>
      <div class="photo photo--children" role="img" aria-label="Photo: four smiling children leaning together against a white backdrop"></div>
      <p class="resources">
        For reliable info on flu:<br>
        Call your doctor<br>
        Go to: http://www.nationalhealthagency.org/flu/<br>
        Call 1-800-555-0142
      </p>
      <div class="sponsor">
        <span class="sponsor__label">Sponsored by:</span>
        <span class="sponsor__name">Hartwell &amp; Lane</span>
      </div>
    </section>

    <section class="panel panel--front">
      <div class="photo photo--patient" role="img" aria-label="Photo: a woman wrapped in a blanket blowing her nose and checking a thermometer"></div>
      <svg class="shapes" width="594" height="768" viewBox="0 0 594 768">
        <polygon points="0,340 594,340 594,404 277,404 242,366 0,366" fill="#29a8e0"/>
        <polygon points="242,366 277,400 594,400 594,404 275,404 240,368" fill="#0f62a8"/>
        <polygon points="275,712 594,712 594,768 0,768 0,750 247,750" fill="#29a8e0"/>
      </svg>
      <h2 class="section-title">KNOW AND DO</h2>
      <p class="question">
        FLU<br>
        What are 4 things I can do to<br>
        prepare for the flu season and<br>
        keep my family healthy?
      </p>
      <ul class="steps">
        <li class="steps__item">Know</li>
        <li class="steps__item">Prevent</li>
        <li class="steps__item">Protect</li>
        <li class="steps__item">Treat</li>
      </ul>
      <p class="credits">©2013. Northfield Health Literacy Team. Northfield University. Marlow T, Ellison JB, Carver DN. Content based on scientific evidence from the Department of Public Health and the National Health Agency (NHA) as of March 2013.</p>
      <div class="sponsor">
        <span class="sponsor__label">Sponsored by:</span>
        <span class="sponsor__name">Hartwell &amp; Lane</span>
      </div>
      <span class="web">www.nationalhealthagency.org/flu</span>
    </section>

  </div>
</div>
</body>
</html>
```